Website Design for Harrowgate & Pellinor LLC

We are looking for a new website design for our law firm. We have provided links to other websites that we find appealing.

```html
<!DOCTYPE html>
<html lang="en">
<head>
<meta charset="utf-8">
<title>Harrowgate &amp; Pellinor LLC – Attorneys at Law</title>
<link rel="stylesheet" href="https://fonts.googleapis.com/css2?family=Caladea:wght@400;700&family=Carlito:wght@400;700&display=swap">
<style>
  :root {
    --bg-center: #e4e8cc;
    --bg-edge: #a9b87f;
    --brown: #4e2814;
    --rust-top: #b9562a;
    --rust-bottom: #6e2a10;
    --green: #56650f;
    --text: #3a3124;
    --box-green: #e5e9cc;
    --box-rose: #ece1dc;
    --nav-top: #ffffff;
    --nav-bottom: #e9e9e6;
    --divider: #d8d8d4;
    --link-green: #4f6314;
  }
  * { box-sizing: border-box; margin: 0; padding: 0; }
  html, body { width: 1200px; height: 800px; overflow: hidden; }
  body {
    position: relative;
    background: radial-gradient(ellipse 70% 70% at 50% 50%, var(--bg-center) 0%, #cdd5a8 55%, var(--bg-edge) 100%);
    font-family: "Carlito", "Calibri", sans-serif;
    color: var(--text);
  }

  /* Navigation */
  .main-nav {
    position: absolute; left: 107px; top: 19px; width: 975px; height: 64px;
    display: flex;
    background: linear-gradient(var(--nav-top), var(--nav-bottom));
    box-shadow: 0 1px 3px rgba(0,0,0,.25);
  }
  .main-nav a {
    display: flex; align-items: center; justify-content: center;
    height: 100%;
    font-size: 13px; font-weight: 700; text-transform: uppercase;
    color: #3b2a1e; text-decoration: none;
    border-right: 1px solid var(--divider);
    position: relative;
  }
  .main-nav a:last-child { border-right: none; }
  .main-nav a.is-active {
    color: #fff;
    background: linear-gradient(var(--rust-top), var(--rust-bottom));
    border-right: none;
  }
  .main-nav a.is-active::after {
    content: ""; position: absolute; left: 50%; bottom: -7px; margin-left: -7px;
    border-left: 7px solid transparent; border-right: 7px solid transparent;
    border-top: 7px solid var(--rust-bottom);
  }

  /* Panel */
  .page-panel {
    position: absolute; left: 107px; top: 96px; width: 975px; height: 577px;
    background: #fff;
    box-shadow: 0 1px 4px rgba(0,0,0,.3);
  }
  .firm-title {
    position: absolute; left: 0; right: 0; top: 28px; text-align: center;
    font-family: "Caladea", "Cambria", serif; color: var(--brown);
  }
  .firm-title h1 { font-size: 38px; font-weight: 700; line-height: 42px; }
  .firm-title p { font-size: 35px; font-weight: 400; line-height: 40px; }

  .box {
    position: absolute; top: 144px; height: 263px; width: 296px;
  }
  .box h2 {
    font-family: "Caladea", "Cambria", serif; font-weight: 700; font-size: 25px;
    height: 58px; line-height: 58px; padding-left: 28px;
    border-bottom: 2px solid #fff;
  }
  .practice { left: 24px; background: var(--box-green); }
  .practice h2 { color: var(--brown); }
  .practice ul { list-style: none; padding: 18px 0 0 34px; }
  .practice li { font-size: 13px; line-height: 24px; }
  .practice li::before { content: "»"; display: inline-block; width: 25px; color: #6a6a55; }

  .feature { left: 334px; width: 295px; background: var(--box-green); }
  .feature-image {
    position: absolute; left: 12px; top: 8px; width: 271px; height: 139px;
    background: linear-gradient(160deg, #b7cce0 0%, #a8694f 45%, #8a4b36 70%, #7f9660 100%);
  }
  .feature h3 { position: absolute; left: 12px; top: 157px; font-size: 13px; font-weight: 700; color: var(--green); }
  .feature p { position: absolute; left: 12px; top: 181px; font-size: 13px; }
  .btn-more {
    position: absolute; left: 12px; top: 219px; width: 93px; height: 29px;
    display: flex; align-items: center; justify-content: center;
    background: linear-gradient(var(--rust-top), var(--rust-bottom));
    color: #fff; font-size: 12.5px; font-weight: 700; text-transform: uppercase;
    text-decoration: none; border: 1px solid #5a200a;
  }

  .contact { left: 645px; width: 295px; background: var(--box-rose); }
  .contact h2 { color: var(--green); }
  .office { position: absolute; left: 38px; font-size: 13px; line-height: 18.5px; width: 230px; }
  .office strong { font-weight: 700; color: #2e241a; }
  .office .send { position: absolute; right: 0; bottom: 0; font-size: 11px; }
  .office .send a { color: var(--brown); font-weight: 700; font-style: italic; }

  .attorney {
    position: absolute; top: 441px; height: 74px; width: 300px;
  }
  .attorney-photo {
    position: absolute; left: 0; top: 0; width: 88px; height: 74px;
    border: 3px solid #fff; box-shadow: 0 0 3px rgba(0,0,0,.35);
    background: linear-gradient(#d9d4cc, #b8aa9c);
  }
  .attorney-info { position: absolute; left: 104px; top: 3px; font-size: 13px; line-height: 17.5px; white-space: nowrap; }
  .attorney-info h4 { font-size: 13px; font-weight: 700; color: var(--green); }

  /* Footer */
  .site-footer {
    position: absolute; left: 0; right: 0; top: 716px; text-align: center;
    font-size: 11px; line-height: 18px; color: #2e2a1e;
  }
  .site-footer a { color: #2e2a1e; text-decoration: none; }
  .site-footer a.is-active { color: var(--link-green); text-decoration: underline; }
</style>
</head>
<body>
  <nav class="main-nav">
    <a href="#" class="is-active" style="width:107px">Home</a>
    <a href="#" style="width:124px">About Us</a>
    <a href="#" style="width:187px">Environmental Law</a>
    <a href="#" style="width:251px">Land Use/ Complex Litigation</a>
    <a href="#" style="width:164px">Corporate Law</a>
    <a href="#" style="width:142px">Contact Us</a>
  </nav>

  <main class="page-panel">
    <header class="firm-title">
      <h1>Harrowgate &amp; Pellinor LLC</h1>
      <p>Attorneys at Law</p>
    </header>

    <section class="box practice">
      <h2>Areas of Practice:</h2>
      <ul>
        <li>Environmental Law</li>
        <li>Land Use Law</li>
        <li>Corporate Law</li>
        <li>Redevelopment</li>
        <li>Complex Business Litigation</li>
        <li>Civil Rights / Housing Law</li>
      </ul>
    </section>

    <section class="box feature">
      <div class="feature-image" role="img" aria-label="Photo of a brick residential and commercial redevelopment building"></div>
      <h3>Residential/Commercial</h3>
      <p>Redevelopment -- Institutional to Mixed</p>
      <a href="#" class="btn-more">View More</a>
    </section>

    <section class="box contact">
      <h2>Contact Us:</h2>
      <div class="office" style="top:80px">
        <strong>NEWYORK CITY:</strong><br>
        215 East 64th Street<br>
        Suite # 902<br>
        New York, NY&nbsp; 10065
        <span class="send">send an <a href="#">email</a></span>
      </div>
      <div class="office" style="top:170px">
        <strong>PRINCETON, NJ:</strong><br>
        88 Linden St.<br>
        Princeton, NJ 08540
        <span class="send">send an <a href="#">email</a></span>
      </div>
    </section>

    <article class="attorney" style="left:25px">
      <div class="attorney-photo" role="img" aria-label="Portrait photo of Martin D. Harrowgate"></div>
      <div class="attorney-info">
        <h4>Environmental Law</h4>
        Martin D. Harrowgate, Esq<br>
        Phone: (609) 555-0148<br>
        martin@harrowgatepellinor.com
      </div>
    </article>
    <article class="attorney" style="left:338px">
      <div class="attorney-photo" role="img" aria-label="Portrait photo of Helen R. Pellinor"></div>
      <div class="attorney-info">
        <h4>Land Use/ Complex Litigations</h4>
        Helen R. Pellinor, Esq.<br>
        Phone: (609) 555-0148<br>
        helen@harrowgatepellinor.com
      </div>
    </article>
    <article class="attorney" style="left:650px">
      <div class="attorney-photo" role="img" aria-label="Portrait photo of Clara J. Whitfield"></div>
      <div class="attorney-info">
        <h4>Corporate Law/ Transactions</h4>
        Clara J. Whitfield, Esq.<br>
        Phone: (609) 555-0148<br>
        clara@harrowgatepellinor.com
      </div>
    </article>
  </main>

  <footer class="site-footer">
    <a href="#" class="is-active">Home</a> &nbsp;|&nbsp; <a href="#">About Us</a> &nbsp;|&nbsp; <a href="#">Environmental Law</a> &nbsp;|&nbsp; <a href="#">Land Use / Complex Litigations</a> &nbsp;|&nbsp; <a href="#">Corporate Law</a> &nbsp;|&nbsp;<a href="#">Contact Us</a><br>
    <a href="#">Disclaimer</a> &nbsp;|&nbsp; <a href="#">Privacy Policy</a><br>
    © Copyrights 2011, All rights reserved.
  </footer>
</body>
</html>
```